Medical Prescription for Diagnostic Sleep Testing

Quiet Harbor Rest Labs main marketing tool is our Prescription that we leave with medical providers. Prescription is printed on 8.5 x 11 sheets of paper to create a prescription pad for our medical providers. Prescription should fit to one page. Quiet Harbor Rest Labs works with 250 different medical providers so it is important we are able to update and change the medical provider information at bottom. The medical provider would fill-out top with patient information, check-off center testing and patient co-morbidity and Fax to Quiet Harbor Rest Labs. Because it is Faxed to us it is important to have clear print and large font Attached or uploaded file is one example we currently use. Please review all 5 must haves.

Target Market(s)

Prescription for medical providers to fill-out and fax to Quiet Harbor Rest Labs to conduct the sleep study.

Industry/Entity Type

Medical

Colors

Designer to choose only greyscale colors for use in the design.

Requirements
Must have
• 1) Prescription Size: 8.5 x 11
• 2) Must fit to One page Only
• 3) Ability to change medical provider information at bottom of prescription. We work with 250 different medical providers
• 4) Ability to change or update any part of prescription
• 5) Document Must be created in Microsoft Word 2016. This is the program we use for our prescriptions.
Nice to have
• Can be done in Gray-Scale or Black and White since its being faxed from the medical provider to us.

```html
<!DOCTYPE html>
<html lang="en">
<head>
<meta charset="utf-8">
<title>Sleep Study Physician Order</title>
<link rel="stylesheet" href="https://fonts.googleapis.com/css2?family=Cinzel:wght@500&family=Open+Sans:ital,wght@0,400;0,600;0,700;1,400&family=Tinos:ital@0;1&family=Archivo+Narrow:ital@0;1&display=swap">
<style>
:root{
  --ink:#111;
  --accent:#6a3c9e;
  --rule:#111;
  --header-bg:#e4e2ee;
  --badge:#6a3c9e;
  --page:#fff;
}
*{box-sizing:border-box;margin:0;padding:0}
html,body{width:927px;height:1200px;overflow:hidden;background:var(--page)}
.page{position:relative;width:927px;height:1200px;color:var(--ink);font-family:"Open Sans",Arial,sans-serif}
.abs{position:absolute;white-space:nowrap}
.box{display:inline-block;width:13px;height:13px;border:1.6px solid var(--ink);box-shadow:2px 2px 0 var(--ink);vertical-align:middle;margin-right:7px;position:relative;top:-2px}
.box.lg{width:16px;height:16px;border-width:2px;box-shadow:2.5px 2.5px 0 var(--ink);margin-right:9px}

/* brand */
.brand{left:22px;top:24px;width:230px;height:134px;display:flex;flex-direction:column;align-items:center;justify-content:center;gap:10px}
.brand-name{font-family:"Open Sans",sans-serif;font-weight:700;color:var(--accent);font-size:25px;line-height:1.15;text-align:center;white-space:normal}
.brand-row{display:flex;align-items:center;gap:8px}
.brand-mark{width:14px;height:14px;background:var(--accent)}
.badge{width:96px;height:22px;border:2px solid var(--badge);border-radius:3px}

.title{left:330px;top:46px;font-family:"Cinzel",serif;font-weight:500;color:var(--accent);font-size:27px;letter-spacing:.3px}
.contact{left:290px;width:600px;text-align:center;font-weight:700;font-size:16.5px}

/* patient fields */
.field{font-family:"Tinos","Times New Roman",serif;font-size:15px;display:flex;align-items:flex-end}
.line{display:inline-block;border-bottom:1px solid var(--ink);height:15px;margin-left:2px}
.rule{left:52px;width:716px;height:2px;background:var(--rule)}

.section-title{left:0;width:927px;text-align:center;font-weight:600;font-size:19px}
.study{font-weight:600;font-size:19px}
.study small{font-family:"Archivo Narrow",sans-serif;font-weight:400;font-size:11.5px}
.sub{font-weight:600;font-size:16px}
.sub small{font-family:"Archivo Narrow",sans-serif;font-weight:400;font-size:11.5px}
.note{font-family:"Archivo Narrow",sans-serif;font-size:11.5px}
.note.i{font-style:italic}
.comply{font-family:"Archivo Narrow",sans-serif;font-style:italic;font-weight:700;font-size:13px;text-decoration:underline}

/* necessity table */
.necessity{left:55px;top:632px;width:849px;height:233px;border:1px solid var(--ink)}
.necessity-head{height:19px;background:var(--header-bg);border-bottom:1px solid var(--ink);text-align:center;font-family:"Tinos",serif;font-weight:700;font-size:14px;line-height:18px}
.necessity-cols{display:grid;grid-template-columns:272px 262px 1fr;height:212px}
.necessity-cols ul{list-style:none;padding:6px 0 0 8px;font-family:"Tinos",serif;font-size:16.5px;line-height:22.8px}
.necessity-cols ul+ul{border-left:1px solid var(--ink)}
.necessity-cols .wrap{padding-left:20px}
.other-line{display:inline-block;width:220px;border-bottom:1px solid var(--ink);height:14px}

.clinic{left:0;width:927px;text-align:center;font-weight:600;font-size:25px}
.clinic-info{left:0;width:927px;text-align:center;font-size:14px}
.provider{font-weight:600;font-size:17px}
.npi{font-family:"Archivo Narrow",sans-serif;font-weight:700;font-size:12.5px}

.sign{font-family:"Tinos",serif;font-size:15px}
.fax{left:0;width:927px;text-align:center;font-weight:700;font-size:16px}
.attach{left:52px;font-size:13.5px}
.thanks{left:0;width:927px;text-align:center;font-family:"Tinos",serif;font-style:italic;font-size:19px}
</style>
</head>
<body>
<main class="page">
  <div class="abs brand">
    <div class="brand-row"><span class="brand-mark"></span><span class="brand-name">Quiet Harbor<br>Rest Labs</span></div>
    <div class="badge" role="img" aria-label="Accreditation badge"></div>
  </div>
  <h1 class="abs title">SLEEP STUDY PHYSICIAN ORDER</h1>
  <p class="abs contact" style="top:89px">Phone: (555) 210-4471 &nbsp;•&nbsp; Fax: (555) 210-4472</p>
  <p class="abs contact" style="top:114px">820 W. Linden Avenue, Suite 2 - C; Fairview, NV 89000</p>

  <div class="abs field" style="left:55px;top:176px">Patient Name:<span class="line" style="width:186px"></span></div>
  <div class="abs field" style="left:462px;top:176px">DOB: <span class="line" style="width:74px"></span>/<span class="line" style="width:74px"></span>/<span class="line" style="width:74px"></span></div>
  <div class="abs field" style="left:55px;top:206px">Telephone: <span class="line" style="width:201px"></span></div>
  <div class="abs field" style="left:383px;top:206px">Alternate Telephone: <span class="line" style="width:223px"></span></div>
  <div class="abs field" style="left:55px;top:236px">Primary Insurance: <span class="line" style="width:156px"></span></div>
  <div class="abs field" style="left:380px;top:236px">Secondary Insurance: <span class="line" style="width:223px"></span></div>
  <div class="abs field" style="left:55px;top:266px">Height:<span class="line" style="width:68px"></span></div>
  <div class="abs field" style="left:176px;top:266px">Weight:<span class="line" style="width:82px"></span></div>
  <div class="abs field" style="left:377px;top:266px">Patient Gender&nbsp;<span style="font-size:8.5px">(circle one)</span>: &nbsp;&nbsp;M &nbsp;&nbsp;/ &nbsp;&nbsp;F</div>

  <div class="abs rule" style="top:302px"></div>
  <h2 class="abs section-title" style="top:306px">Diagnostic Sleep Study Ordered</h2>

  <p class="abs study" style="left:86px;top:344px"><span class="box lg"></span><u>COMPLETE SLEEP STUDY</u>: <span style="font-weight:400;font-style:italic;font-size:17px;text-decoration:underline dotted">(Based on Insurance or Patient’s Choice)</span></p>
  <p class="abs sub" style="left:121px;top:377px">In-Lab Sleep Study (PSG) or Home Sleep Study <small>(PSG 95810 / HST 95806)</small></p>
  <p class="abs sub" style="left:123px;top:403px">with follow-up PAP Titration Study <small>(PAP 95811 if positive for sleep apnea)</small></p>

  <p class="abs study" style="left:91px;top:431px"><span class="box lg"></span>PEDIATRIC SLEEP STUDY: PSG w/End Tidal CO2 Monitoring</p>
  <p class="abs note" style="left:122px;top:459px">(PSG 95782 under 6 years of age &amp; PSG 95810 older than 6 years of age)</p>
  <p class="abs study" style="left:91px;top:477px"><span class="box lg"></span>In-Lab Diagnostic Sleep Study/Polysomnogram <small>(PSG 95810)</small></p>
  <p class="abs study" style="left:91px;top:508px"><span class="box lg"></span>SPLIT-NIGHT STUDY <small>(PSG with PAP 95810 &amp; 95811)</small> <span class="comply">To Comply With Accreditation &amp; Insurance Guidelines</span>:</p>
  <p class="abs note i" style="left:122px;top:539px">AHI must be 20 or greater with minimum 2 hour recorded sleep time and 3 hours minimum to complete PAP treatment.</p>
  <p class="abs study" style="left:91px;top:559px"><span class="box lg"></span>CPAP / BiPAP / BiPAP ST Titration Study <small>(Patients with documented sleep apnea 95811)</small></p>
  <p class="abs study" style="left:91px;top:589px"><span class="box lg"></span>Home Sleep Study <small>(HST 95806 Conducted in patient’s home &amp; unattended by technologist) (No insurance patient cost $250.00)</small></p>

  <div class="abs rule" style="top:626px"></div>

  <section class="abs necessity">
    <div class="necessity-head">Patient Medical Necessity – Please Check All Boxes That Apply</div>
    <div class="necessity-cols">
      <ul>
        <li><span class="box"></span>Atrial Fibrillation</li>
        <li><span class="box"></span>Bipolar Disorder</li>
        <li><span class="box"></span>Congestive Heart Failure</li>
        <li><span class="box"></span>COPD</li>
        <li><span class="box"></span>Depression</li>
        <li><span class="box"></span>Excessive Daytime Sleepiness</li>
        <li><span class="box"></span>Gasping Sensations with</li>
        <li class="wrap">Frequent Awakenings</li>
        <li><span class="box"></span>Frequent Urination</li>
      </ul>
      <ul>
        <li><span class="box"></span>Heart Disease</li>
        <li><span class="box"></span>History Heart Attack</li>
        <li><span class="box"></span>Hypertension</li>
        <li><span class="box"></span>Insomnia</li>
        <li><span class="box"></span>Mental or Mood Disorder</li>
        <li><span class="box"></span>Loud Snoring</li>
        <li><span class="box"></span>Morbid Obesity / Obesity</li>
        <li><span class="box"></span>Morning Headaches</li>
        <li><span class="box"></span>Narcolepsy</li>
      </ul>
      <ul>
        <li><span class="box"></span>Opioid Use</li>
        <li><span class="box"></span>PTSD</li>
        <li><span class="box"></span>Pulmonary Disease</li>
        <li><span class="box"></span>Restless Leg Syndrome</li>
        <li><span class="box"></span>Seizures</li>
        <li><span class="box"></span>Shift Work Sleep disorder</li>
        <li><span class="box"></span>Stroke / TIA</li>
        <li><span class="box"></span>Witnessed Apnea</li>
        <li><span class="box"></span>Other:<span class="other-line"></span></li>
      </ul>
    </div>
  </section>

  <div class="abs rule" style="top:874px"></div>
  <h2 class="abs clinic" style="top:877px">Cedar Valley Ear + Sinus Clinic</h2>
  <p class="abs clinic-info" style="top:913px">415 E. Orchard Road; Fairview, NV 89001-1000 &nbsp;•&nbsp; Telephone:&nbsp; 555-300-1180 &nbsp;&nbsp;&nbsp;Fax:&nbsp; 555-300-1181</p>

  <p class="abs provider" style="left:56px;top:938px"><span class="box lg"></span>Dr. Adrian Paul Moreno</p>
  <p class="abs npi" style="left:83px;top:965px">NPI:&nbsp; 1000000011</p>
  <p class="abs provider" style="left:330px;top:938px"><span class="box lg"></span>Dr. Daniel R. Hollis</p>
  <p class="abs npi" style="left:357px;top:965px">NPI: 1000000022</p>
  <p class="abs provider" style="left:603px;top:938px"><span class="box lg"></span>Dr Gregory M. Lindqvist</p>
  <p class="abs npi" style="left:627px;top:965px">NPI: 1000000033</p>

  <p class="abs provider" style="left:56px;top:985px"><span class="box lg"></span>Dr. Helen Park</p>
  <p class="abs npi" style="left:80px;top:1011px">NPI: 1000000044</p>
  <p class="abs provider" style="left:330px;top:985px"><span class="box lg"></span>Maria Ellison, FNP-C</p>
  <p class="abs npi" style="left:354px;top:1011px">NPI: 1000000055</p>
  <p class="abs provider" style="left:603px;top:985px"><span class="box lg"></span>Neil Barton, PA-C</p>
  <p class="abs npi" style="left:624px;top:1011px">NPI: 1000000066</p>

  <div class="abs field sign" style="left:33px;top:1073px">Physician’s Signature:<span class="line" style="width:454px"></span>&nbsp;Date: <span class="line" style="width:64px"></span>/<span class="line" style="width:64px"></span>/<span class="line" style="width:64px"></span></div>
  <p class="abs fax" style="top:1098px">Please Fax: 555-210-4472 or Email: intake@quietharborrest.example</p>
  <p class="abs attach" style="top:1123px"><svg width="14" height="14" viewBox="0 0 14 14" style="vertical-align:-1px;margin-right:4px"><rect x="1" y="2" width="11" height="11" fill="none" stroke="#111" stroke-width="1"/><path d="M3.5 7.5 L6 10.5 L12.5 1.5" fill="none" stroke="#111" stroke-width="1.2"/></svg>Fax Along With: Patient Demographic Information &nbsp;•&nbsp; Copy of Current Insurance Information &nbsp;•&nbsp; Clinical Notes</p>
  <p class="abs thanks" style="top:1150px">Thank You For your support ELLIS &amp; MARA</p>
</main>
</body>
</html>
```